'Bright Ledger Hidden Keys' Book Cover

I need a professional book cover design for my new upcoming book that shows people how to get a high credit score.

Here are my two websites:

https://www.moneywordbank-lexa.info
https://moneywordbank-lexa.com/

I am looking for a clean, professional design that pops (emotional touch) and separates from the other books that are on the market. Cover aspect ratio 1:4 for Pagewisp version and 1:5 for the paperback version. Yellow or blue are good colors - but not must. See the basic examples that I provided. File delivery format PDF.

Book Title: Bright Ledger Hidden Keys
Byline: The Quick Lift And Mend Manual for Stellar Borrowing

Currently on Brindlecart pre-order:
https://www.brindlecart.example/Bright-Ledger-Hidden-Keys-Stellar-ebook/dp/Q48MPLRT71

I am the author of 36 published books on Brindlecart. My author profile is here:
brindlecart.example/author/gideonvarly

Targeted audience: People that want to improve or repair their bad credit score.

Target Market(s)

People/consumers in the US that want to improve or repair their credit score.

Industry/Entity Type

Consumer

Font styles to use
Sans Serif

Colors

Designer to choose colors to be used in the design.

Requirements
Must have
• Author name, Title, byline, and graphic element(s).
Nice to have
• - 2020 edition logo / batch

```html
<!DOCTYPE html>
<html lang="en">
<head>
<meta charset="UTF-8">
<title>Bright Ledger Hidden Keys – Book Cover</title>
<link href="https://fonts.googleapis.com/css2?family=Anton&family=Oswald:wght@700&family=Questrial&display=swap" rel="stylesheet">
<style>
  :root {
    --page-bg: #f4f4f4;
    --cover-yellow: #e6e414;
    --cover-yellow-light: #eeec3a;
    --title-blue: #0a67b0;
    --band-blue: #0b69b3;
    --ink: #111111;
    --glow: #f8f5d2;
    --photo-warm: #e0a08c;
    --photo-deep: #c9443c;
  }
  * { margin: 0; padding: 0; box-sizing: border-box; }
  html, body {
    width: 1200px;
    height: 800px;
    overflow: hidden;
    background: var(--page-bg);
  }
  .stage {
    position: relative;
    width: 1200px;
    height: 800px;
  }
  .cover {
    position: absolute;
    left: 375px;
    top: 30px;
    width: 450px;
    height: 740px;
    overflow: hidden;
    background: linear-gradient(100deg, var(--cover-yellow-light) 0%, var(--cover-yellow) 30%, #e0de14 100%);
    box-shadow: 0 14px 30px rgba(0,0,0,0.18);
  }
  .cover__band {
    position: absolute;
    left: 0;
    bottom: 0;
    width: 100%;
    height: 142px;
    background: var(--band-blue);
  }
  .cover__author {
    position: absolute;
    top: 10px;
    width: 100%;
    text-align: center;
    font-family: "Oswald", sans-serif;
    font-weight: 700;
    font-size: 34px;
    letter-spacing: 3px;
    color: var(--ink);
    line-height: 1.2;
  }
  .cover__title {
    position: absolute;
    top: 72px;
    width: 100%;
    text-align: center;
    font-family: "Anton", sans-serif;
    font-weight: 400;
    color: var(--title-blue);
    text-transform: uppercase;
    letter-spacing: 1px;
  }
  .cover__title-line { display: block; line-height: 0.94; }
  .cover__title-line--one { font-size: 64px; }
  .cover__title-line--two { font-size: 94px; }
  .cover__title-line--three { font-size: 94px; }
  .cover__subtitle {
    position: absolute;
    top: 326px;
    width: 100%;
    padding: 0 24px;
    text-align: center;
    font-family: "Questrial", sans-serif;
    font-size: 19px;
    line-height: 1.3;
    color: var(--ink);
    text-transform: uppercase;
  }
  .cover__photo {
    position: absolute;
    left: 95px;
    top: 384px;
    width: 270px;
    height: 356px;
  }
</style>
</head>
<body>
  <main class="stage">
    <section class="cover">
      <div class="cover__band"></div>

      <svg class="cover__photo" viewBox="0 0 270 356" role="img" aria-label="Photo of a smiling young woman in a red sweater holding up a credit card, lit by a soft glow">
        <defs>
          <radialGradient id="photoFill" cx="50%" cy="40%" r="70%">
            <stop offset="0%" stop-color="var(--glow)"/>
            <stop offset="55%" stop-color="var(--photo-warm)"/>
            <stop offset="100%" stop-color="var(--photo-deep)"/>
          </radialGradient>
        </defs>
        <rect x="0" y="0" width="270" height="356" rx="18" fill="url(#photoFill)"/>
      </svg>

      <p class="cover__author">GIDEON VARLY</p>

      <h1 class="cover__title">
        <span class="cover__title-line cover__title-line--one">Bright Ledger</span>
        <span class="cover__title-line cover__title-line--two">Hidden</span>
        <span class="cover__title-line cover__title-line--three">Keys</span>
      </h1>

      <p class="cover__subtitle">The Quick Lift And Mend Manual<br>for Stellar Borrowing</p>
    </section>
  </main>
</body>
</html>
```